New Dental Office Needs an Attractive and user friendly Website Designed

I need a website for a new dental office. The Name is Maplecrest Dentistry. I would like a Modern design with a user friendly interface and usability.
I would like a landing page, a page that lists the services we offer: Cosmetic Dentistry, Implants, Dental Hygiene, Emergency Services, Restorations, Dentures
Target Market(s)
Mid to upper class
Industry/Entity Type
Dentistry
Coding
Coded - Design and coding required
Number of Pages Required
1 page
Requirements
Must have
- Landing page that has a scheduling option, Procedures, operating hours, and contact us info
Nice to have
- Appealing design, Soft comforting colors. Easy to navigate page, Modern and professional.

```html
<!DOCTYPE html>
<html lang="en">
<head>
<meta charset="utf-8">
<title>Maplecrest Dentistry</title>
<link href="https://fonts.googleapis.com/css2?family=Jost:wght@400;500;600&family=Poppins:wght@400;500;600;700&display=swap" rel="stylesheet">
<style>
:root{
  --blue:#0aa0dc;
  --green:#8dc63f;
  --dark:#232323;
  --ink:#222;
  --muted:#555;
  --cream:#eeede6;
  --white:#fff;
}
*{box-sizing:border-box;margin:0;padding:0}
html,body{width:1200px;height:3964px;overflow:hidden}
body{position:relative;font-family:'Poppins',sans-serif;color:var(--ink);background:var(--white)}
.abs{position:absolute}
.btn{position:absolute;display:flex;align-items:center;justify-content:center;gap:8px;color:#fff;font-size:13px;font-weight:600;text-transform:uppercase;border-radius:0 16px 0 16px}
.btn.green{background:var(--green)}
.btn.blue{background:var(--blue)}
.arrow-dot{width:12px;height:12px;border-radius:50%;background:#fff;display:inline-block;position:relative}
.arrow-dot::after{content:"";position:absolute;left:3px;top:3px;border-left:5px solid currentColor;border-top:3px solid transparent;border-bottom:3px solid transparent}
.btn.green .arrow-dot{color:var(--green)} .btn.blue .arrow-dot{color:var(--blue)}

/* top bar */
.topbar{left:0;top:0;width:1200px;height:46px;background:var(--dark);color:#fff;font-size:13px;font-weight:500}
.topbar .hours{left:110px;top:14px}
.topbar .call{left:700px;top:14px}
.social{position:absolute;top:0;width:36px;height:46px;border-left:1px solid #444;display:flex;align-items:center;justify-content:center}
.social span{width:12px;height:12px;border:2px solid #fff;border-radius:3px}
.social.active{background:var(--green)}

/* header */
.nav a{position:absolute;top:94px;font-size:14px;font-weight:500;color:var(--ink);text-decoration:none}
.nav a.current{color:var(--green);border-bottom:2px solid var(--green);padding-bottom:2px}
.logo{left:460px;top:74px;width:280px;text-align:center;font-family:'Jost',sans-serif;font-weight:500;font-size:30px;line-height:1.05;color:var(--ink)}

/* hero */
.hero-photo{left:0;top:158px;width:1200px;height:640px;background:linear-gradient(100deg,#c9d6df 0%,#e8e2dc 30%,#eef0f2 60%,#dfe6ec 100%)}
.hero-text{left:590px;top:306px;width:506px;text-align:center}
.hero-text .kicker{font-family:'Jost',sans-serif;font-size:26px;color:var(--blue);font-weight:500}
.hero-text h1{font-family:'Jost',sans-serif;font-weight:500;font-size:42px;line-height:1.2;margin-top:10px}
.hero-text p{font-size:22px;line-height:1.4;margin-top:4px;color:#333}
.slider-dots span{position:absolute;left:1134px;width:15px;height:15px;border:2px solid #333;border-radius:50%}

/* about */
.about{left:0;top:760px;width:1200px;height:642px;background:var(--blue)}
.ring{border-radius:50%;background:var(--green)}
.photo{background:linear-gradient(135deg,#e7c9b4,#9bb8cc 60%,#4b7fa6)}
.about-text{left:650px;top:890px;width:426px;color:#fff}
.about-text h2{font-family:'Jost',sans-serif;font-weight:500;font-size:38px;line-height:1.2}
.underline{width:72px;height:4px;background:var(--green);margin-top:6px}
.about-text p{font-size:15px;line-height:25px;margin-top:22px;text-align:justify}
.about-text p + p{margin-top:14px}

/* section titles */
.sec-title{left:0;width:1200px;text-align:center}
.sec-title .ghost{font-family:'Jost',sans-serif;font-size:82px;font-weight:600;color:#f3f3f3;line-height:1}
.sec-title h2{font-family:'Jost',sans-serif;font-size:38px;font-weight:500;margin-top:-44px}
.sec-title .underline{margin:4px auto 0}

/* procedures */
.card{position:absolute;top:1600px;width:304px;text-align:center}
.card.featured{background:var(--cream);height:470px;border-radius:0 0 0 40px}
.card .img{height:222px;border-radius:0 40px 0 40px}
.card h3{font-size:19px;font-weight:600;margin-top:28px}
.card p{font-size:15px;line-height:25px;color:#333;margin:14px 18px 0}
.card .btn{left:76px;top:402px;width:154px;height:42px}
.car-arrow{position:absolute;top:1697px;width:28px;height:28px;border-radius:50%}

/* testimonials */
.testi{left:0;top:2162px;width:1200px;height:565px;background:linear-gradient(90deg,#84c034,#9bcc4d 50%,#86c13a)}
.testi .ghost{color:rgba(255,255,255,.12)}
.testi h2{color:#fff}
.tcard{position:absolute;top:2353px;width:408px;height:238px;background:#fff;border-radius:0 40px 0 40px;padding:28px 30px 0 77px}
.quote{font-family:'Jost',sans-serif;font-size:54px;line-height:30px;color:var(--green);font-weight:600}
.tcard p{font-size:13.5px;line-height:22px;color:#333;text-align:justify;margin-top:6px}
.tcard .name{color:var(--blue);font-weight:600;font-size:15px;margin-top:6px}
.stars{color:#f5a623;font-size:11px;letter-spacing:1px}
.avatar{position:absolute;width:104px;height:104px;border-radius:50%;background:linear-gradient(135deg,#b9d98d,#6d8c9e);border:8px solid #fff;box-shadow:0 0 0 1px #ddd}
.tdots span{position:absolute;top:2636px;width:15px;height:15px;border:2px solid #fff;border-radius:50%}
.tdots span.on{background:#fff}

/* contact */
.form label{position:absolute;font-size:15px;font-weight:500}
.form .field{position:absolute;height:40px;border:1px solid #eee;box-shadow:0 2px 6px rgba(0,0,0,.08);font-size:13px;color:#666;padding:11px 18px}

/* footer */
.footer{left:0;top:3580px;width:1200px;height:384px;background:var(--dark);color:#fff}
.fcol h4{position:absolute;top:3616px;font-size:18px;font-weight:600;text-transform:uppercase;color:#fff}
.flist{position:absolute;top:3662px;list-style:none;font-size:15px;color:#fff}
.flist li{height:36px;display:flex;align-items:center;gap:22px;white-space:nowrap}
.flist li::before{content:"";width:13px;height:13px;border-radius:50%;background:var(--green);flex:none}
.cinfo{position:absolute;left:564px;font-size:12px;line-height:18px;color:#fff}
.cinfo b{display:block;font-size:14px;font-weight:600;margin-bottom:4px}
.cicon{position:absolute;left:505px;width:36px;height:36px;border-radius:50%;background:#fff;display:flex;align-items:center;justify-content:center;color:var(--green);font-size:16px}
.fsocial{position:absolute;top:3922px;width:34px;height:34px;border-radius:50%;border:2px solid #fff}
.fsocial.active{background:var(--green);border-color:var(--green)}
</style>
</head>
<body>

<!-- top bar -->
<div class="abs topbar">
  <div class="abs hours">&#9993;&nbsp; Operating Hours: Mon–Fri: 8am–6pm, Sat: 9am–2pm, Sun: Closed</div>
  <div class="abs call"><span style="color:var(--blue)">&#9742;</span> Call Us: +1 (555) 204 7781</div>
  <div class="social active" style="left:940px"><span></span></div>
  <div class="social" style="left:976px"><span></span></div>
  <div class="social" style="left:1012px"><span></span></div>
  <div class="social" style="left:1048px;border-right:1px solid #444"><span></span></div>
</div>

<!-- header -->
<nav class="nav">
  <a href="#" class="current" style="left:110px">Home</a>
  <a href="#" style="left:179px">About</a>
  <a href="#" style="left:248px">Procedures</a>
  <a href="#" style="left:356px">Resources</a>
  <a href="#" style="left:764px;top:96px">Contact</a>
</nav>
<div class="abs logo">Maplecrest<br><span style="font-size:17px;letter-spacing:4px">DENTISTRY</span></div>
<div class="btn blue" style="left:857px;top:86px;width:231px;height:42px">&#128197; Book an Appointment</div>

<!-- hero -->
<div class="abs hero-photo" role="img" aria-label="Smiling woman in a dental chair during a check-up with a dentist"></div>
<div class="abs hero-text">
  <div class="kicker">Your Smile, Our Passion</div>
  <h1>Modern Dental Care in a Comforting Environment.</h1>
  <p>Lorem ipsum dolor sit amet, consectetur adi sed do eiusmod tempor</p>
</div>
<div class="btn green" style="left:775px;top:528px;width:136px;height:42px">&#9742; Call Now</div>
<div class="slider-dots">
  <span style="top:385px"></span>
  <span style="top:410px;background:var(--green);border-color:var(--green)"></span>
  <span style="top:435px"></span>
  <span style="top:460px"></span>
</div>

<!-- about -->
<div class="abs about"></div>
<svg class="abs" style="left:0;top:620px" width="1200" height="200" viewBox="0 0 1200 200">
  <path d="M0,170 C220,40 480,100 680,125 C900,150 1100,90 1200,20 L1200,200 L0,200Z" fill="#fff"/>
  <path d="M0,190 C240,70 480,140 700,150 C920,158 1100,100 1200,45 L1200,200 L0,200Z" fill="var(--blue)"/>
</svg>
<div class="abs ring" style="left:111px;top:846px;width:490px;height:490px"></div>
<div class="abs photo" style="left:154px;top:873px;width:440px;height:440px;border-radius:50%" role="img" aria-label="Patient receiving a teeth whitening treatment with a curing light"></div>
<div class="abs about-text">
  <h2>About Maplecrest Dentistry</h2>
  <div class="underline"></div>
  <p>Lorem ipsum dolor sit amet, consectetur adipiscing elit, sed do eiusmod tempor incididunt ut labore et dolore magna aliqua. Ut enim ad minim veniam, quis nostrud exercitation ullamco laboris nisi ut aliquip ex ea commodo enim ad minim veniam consequat.</p>
  <p>Duis aute irure dolor in reprehenderit in voluptate velit esse cillum dolore eu fugiat nulla pariatur. Excepteur sint occaecat cupiea.</p>
</div>
<div class="btn green" style="left:650px;top:1244px;width:154px;height:40px">Learn More <span class="arrow-dot"></span></div>

<!-- procedures -->
<div class="abs sec-title" style="top:1466px">
  <div class="ghost">Our Procedures</div>
  <h2>Our Procedures</h2>
  <div class="underline"></div>
</div>
<div class="car-arrow" style="left:42px;background:#bbb"></div>
<div class="car-arrow" style="left:1130px;background:var(--green)"></div>

<div class="card" style="left:111px">
  <div class="img" style="background:linear-gradient(135deg,#e9cfc4,#c7d6e3)" role="img" aria-label="Woman checking her smile after cosmetic dental work"></div>
  <h3>COSMETIC DENTISTRY</h3>
  <p>Lorem ipsum dolor sit amet, consectetur adipiscing elit, sed do eiusmod tempor incididunt ut labore et dolorea.</p>
  <div class="btn green">Learn More <span class="arrow-dot"></span></div>
</div>
<div class="card featured" style="left:448px">
  <div class="img" style="background:linear-gradient(135deg,#f2d3c7,#eaf3f8 60%,#bfe3f4)" role="img" aria-label="Close-up of a smile with a dental implant detail"></div>
  <h3>IMPLANTS</h3>
  <p>Lorem ipsum dolor sit amet, consectetur adipiscing elit, sed do eiusmod tempor incididunt ut labore et dolorea.</p>
  <div class="btn blue">Learn More <span class="arrow-dot"></span></div>
</div>
<div class="card" style="left:785px">
  <div class="img" style="background:linear-gradient(135deg,#9fc3de,#e1c4ad 55%,#3d7fc1)" role="img" aria-label="Smiling man during a dental hygiene cleaning"></div>
  <h3>DENTAL HYGIENE</h3>
  <p>Lorem ipsum dolor sit amet, consectetur adipiscing elit, sed do eiusmod tempor incididunt ut labore et dolorea.</p>
  <div class="btn green">Learn More <span class="arrow-dot"></span></div>
</div>

<!-- testimonials -->
<div class="abs testi" role="img" aria-label="Green tinted background of a smiling patient"></div>
<div class="abs sec-title testi" style="top:2226px;height:auto;background:none">
  <div class="ghost">Testimonials</div>
  <h2>Testimonials</h2>
  <div class="underline" style="background:#fff"></div>
</div>
<div class="tcard" style="left:180px">
  <div class="quote">&ldquo;</div>
  <p>Lorem ipsum dolor sit amet, consectetur adipiscing elit, sed do eiusmod tempor incididunt ut labore et dolore magna aliqua. Ut enim ad minim veniam, quis nost exercitation ullamcoea.</p>
  <div class="name">- DANA WHITFIELD</div>
  <div class="stars">&#9733;&#9733;&#9733;&#9733;&#9733;</div>
</div>
<div class="avatar" style="left:130px;top:2421px" role="img" aria-label="Patient portrait"></div>
<div class="tcard" style="left:667px">
  <div class="quote">&ldquo;</div>
  <p>Lorem ipsum dolor sit amet, consectetur adipiscing elit, sed do eiusmod tempor incididunt ut labore et dolore magna aliqua. Ut enim ad minim veniam, quis nost exercitation ullamcoea.</p>
  <div class="name">- DANA WHITFIELD</div>
  <div class="stars">&#9733;&#9733;&#9733;&#9733;&#9733;</div>
</div>
<div class="avatar" style="left:617px;top:2421px" role="img" aria-label="Patient portrait"></div>
<div class="tdots">
  <span style="left:555px"></span><span class="on" style="left:580px"></span><span style="left:605px"></span><span style="left:630px"></span>
</div>

<!-- contact -->
<div class="abs sec-title" style="top:2800px">
  <div class="ghost">Get In Touch</div>
  <h2>Get In Touch</h2>
  <div class="underline"></div>
</div>
<div class="abs ring" style="left:100px;top:2933px;width:430px;height:430px"></div>
<div class="abs photo" style="left:134px;top:2960px;width:390px;height:390px;border-radius:50%;background:linear-gradient(135deg,#f4f4f4,#dcdfe2 60%,#b9bec3)" role="img" aria-label="Bright modern treatment room with a dental chair"></div>
<div class="form">
  <label style="left:590px;top:2970px">First Name</label>
  <label style="left:849px;top:2970px">Last Name</label>
  <div class="field" style="left:590px;top:2999px;width:250px">Your First Name</div>
  <div class="field" style="left:849px;top:2999px;width:250px">Your Last Name</div>
  <label style="left:590px;top:3054px">Email</label>
  <label style="left:849px;top:3054px">Phone</label>
  <div class="field" style="left:590px;top:3083px;width:250px">Your Email</div>
  <div class="field" style="left:849px;top:3083px;width:250px">Your Phone</div>
  <label style="left:590px;top:3136px">Comment</label>
  <div class="field" style="left:590px;top:3165px;width:509px;height:95px">Enter Your Comment</div>
</div>
<div class="btn blue" style="left:595px;top:3292px;width:164px;height:41px">Send Message <span class="arrow-dot"></span></div>

<!-- footer -->
<svg class="abs" style="left:0;top:3410px" width="1200" height="200" viewBox="0 0 1200 200">
  <path d="M0,170 C260,10 560,60 790,110 C980,150 1120,70 1200,20 L1200,60 C1120,150 980,180 790,150 C560,110 280,70 0,200Z" fill="var(--blue)"/>
  <path d="M0,200 C280,90 560,130 790,160 C980,185 1120,120 1200,75 L1200,200Z" fill="var(--dark)"/>
</svg>
<div class="abs footer"></div>
<div class="fcol">
  <h4 style="left:110px">Navigation</h4>
  <h4 style="left:292px">Procedures</h4>
  <h4 style="left:505px">Contact Us</h4>
  <h4 style="left:796px">Newsletter</h4>
</div>
<ul class="flist" style="left:110px">
  <li>Home</li><li>About</li><li>Procedures</li><li>Resources</li><li>Contact Us</li><li>FAQs</li>
</ul>
<ul class="flist" style="left:292px">
  <li>Cosmetic Dentistry</li><li>Implants</li><li>Dental Hygiene</li><li>Emergency Services</li><li>Restorations</li><li>Dentures</li>
</ul>
<div class="cicon" style="top:3668px">&#9679;</div>
<div class="cinfo" style="top:3674px"><b>LOCATIONS:</b><span style="font-size:11.5px">212 Alder Grove Lane, Riverton,<br>United States</span></div>
<div class="cicon" style="top:3750px">&#9742;</div>
<div class="cinfo" style="top:3756px"><b>PHONE:</b>+1 (555) 204 7781</div>
<div class="cicon" style="top:3828px">&#9993;</div>
<div class="cinfo" style="top:3820px"><b>OPERATING HOURS:</b><span style="font-size:11.5px">Mon–Fri: 8am–6pm, Sat: 9am–2pm<br>Sun: Closed</span></div>
<div class="abs" style="left:796px;top:3666px;width:293px;height:43px;background:#fff;border-radius:0 16px 0 16px;color:#333;font-size:14px;padding:12px 16px">Email Address</div>
<div class="abs" style="left:796px;top:3722px;width:293px;height:45px;background:var(--blue);border-radius:0 16px 0 16px;color:#fff;font-size:15px;font-weight:600;text-align:center;line-height:45px">SUBSCRIBE</div>
<div class="abs" style="left:110px;top:3905px;width:980px;height:1px;background:#444"></div>
<div class="abs" style="left:0;top:3930px;width:1200px;text-align:center;color:#fff;font-size:13px">© 2025 Maplecrest Dentistry &nbsp;| &nbsp; All Rights Reserved</div>
<div class="fsocial" style="left:934px"></div>
<div class="fsocial active" style="left:975px"></div>
<div class="fsocial" style="left:1016px"></div>
<div class="fsocial" style="left:1057px"></div>

</body>
</html>
```